Startup internet service provider needs a good facebook ad

Looking for a catchy facebook ad to launch our internet service in Parker, Colorado. Short video or slideshow preferred, still pictures are okay.

https://www.facebook.com/BrimfoxNetworks

www.brimfox-networks.example

Target Market(s)

Parker Colorado

Colors
add136
0255a3

```html
<!DOCTYPE html>
<html lang="en">
<head>
<meta charset="utf-8">
<title>Brimfox Networks – Launch Slides</title>
<link rel="stylesheet" href="https://fonts.googleapis.com/css2?family=Poppins:wght@400;500;600;700&display=swap">
<style>
  :root{
    --brand-blue:#0255a3;
    --deep-blue:#0a3f8c;
    --navy:#062f6e;
    --lime:#add136;
    --lime-bright:#c4dc37;
    --white:#ffffff;
    --gold:#d9b84a;
  }
  *{margin:0;padding:0;box-sizing:border-box}
  html,body{width:1200px;height:474px;overflow:hidden;background:var(--brand-blue)}
  body{font-family:"Poppins",sans-serif;position:relative}
  .board{position:relative;width:1200px;height:474px}
  .slide-label{
    position:absolute;top:44px;width:200px;margin-left:-100px;text-align:center;
    color:var(--lime-bright);font-weight:700;font-size:27px;letter-spacing:.5px;line-height:1;
  }
  .slide{
    position:absolute;top:84px;width:341px;height:339px;overflow:hidden;
    box-shadow:0 4px 10px rgba(0,20,60,.35);
  }
  .slide-art{position:absolute;inset:0;width:341px;height:339px}
  .headline{
    position:absolute;left:0;right:0;top:14px;text-align:center;font-weight:700;line-height:1.05;
  }
  .headline .accent{color:var(--lime-bright);display:block}
  .headline .main{color:var(--white);display:block}
  .headline .sub{display:block;color:var(--white);font-weight:500;font-size:7.2px;margin-top:4px}
  .feature{position:absolute;color:var(--white);font-weight:600;font-size:7.6px;line-height:1.1}
  .feature .hl{color:var(--lime-bright);border-bottom:1px solid var(--lime-bright)}
  .feature-support{left:18px;top:110px}
  .feature-speed{right:17px;top:116px;text-align:left}
  .brand-tag{
    position:absolute;left:0;top:300px;width:115px;height:24px;background:var(--white);
    border-radius:0 4px 4px 0;display:flex;align-items:center;padding-left:22px;gap:4px;
  }
  .brand-tag .dot{width:9px;height:9px;border-radius:50%;background:var(--brand-blue)}
  .brand-tag .name{color:var(--brand-blue);font-size:6.6px;font-weight:500}
  .contact{position:absolute;left:211px;top:303px;display:flex;align-items:center;gap:3px}
  .contact svg{width:13px;height:19px}
  .contact .lines{line-height:1}
  .contact .cta{color:var(--brand-blue);font-size:7.4px;font-weight:500;display:block}
  .contact .phone{color:var(--brand-blue);font-size:14.5px;font-weight:700;display:block;letter-spacing:.2px}
</style>
</head>
<body>
<main class="board">

  <!-- Slide 01 -->
  <div class="slide-label" style="left:220px">SLIDE 01</div>
  <section class="slide" style="left:67px">
    <svg class="slide-art" viewBox="0 0 341 339" aria-hidden="false">
      <defs>
        <linearGradient id="bg1" x1="0" y1="0" x2="0" y2="1"><stop offset="0" stop-color="#0a4aa0"/><stop offset=".6" stop-color="#073d8a"/></linearGradient>
        <radialGradient id="photo1" cx=".5" cy=".55" r=".6"><stop offset="0" stop-color="#c9a98a"/><stop offset=".6" stop-color="#9c7a68"/><stop offset="1" stop-color="#6e5a56"/></radialGradient>
      </defs>
      <rect width="341" height="339" fill="url(#bg1)"/>
      <path d="M0,168 C45,258 110,300 170,300 C230,300 296,258 341,168 L341,339 L0,339 Z" fill="#ffffff"/>
      <path d="M0,192 C55,270 115,312 170,312 C225,312 290,272 341,192 L341,339 L0,339 Z" fill="var(--lime-bright)"/>
      <circle cx="170" cy="189" r="114" fill="none" stroke="var(--gold)" stroke-width=".7"/>
      <circle cx="170" cy="189" r="108" fill="var(--deep-blue)"/>
      <circle cx="170" cy="189" r="105" fill="url(#photo1)" role="img" aria-label="Photo of a family on a sofa using a tablet, laptop and phone"/>
      <g fill="#c8d6ee"><circle cx="18" cy="15" r=".8"/><circle cx="23" cy="15" r=".8"/><circle cx="28" cy="15" r=".8"/><circle cx="33" cy="15" r=".8"/><circle cx="18" cy="20" r=".8"/><circle cx="23" cy="20" r=".8"/><circle cx="28" cy="20" r=".8"/><circle cx="33" cy="20" r=".8"/><circle cx="18" cy="25" r=".8"/><circle cx="23" cy="25" r=".8"/><circle cx="28" cy="25" r=".8"/><circle cx="33" cy="25" r=".8"/>
      <circle cx="310" cy="15" r=".8"/><circle cx="315" cy="15" r=".8"/><circle cx="320" cy="15" r=".8"/><circle cx="325" cy="15" r=".8"/><circle cx="310" cy="20" r=".8"/><circle cx="315" cy="20" r=".8"/><circle cx="320" cy="20" r=".8"/><circle cx="325" cy="20" r=".8"/><circle cx="310" cy="25" r=".8"/><circle cx="315" cy="25" r=".8"/><circle cx="320" cy="25" r=".8"/><circle cx="325" cy="25" r=".8"/></g>
    </svg>
    <h2 class="headline"><span class="accent" style="font-size:22px">Fast and Reliable</span><span class="main" style="font-size:22px">Internet Service</span><span class="sub">designed and catered to meet your needs</span></h2>
    <p class="feature feature-support">Real<br>Customer<br><span class="hl">Support</span></p>
    <p class="feature feature-speed">Fast Web<br><span class="hl">Browsing</span></p>
    <div class="brand-tag"><span class="dot"></span><span class="name">Brimfox Networks</span></div>
    <div class="contact">
      <svg viewBox="0 0 13 19"><rect width="13" height="19" rx="1.5" fill="var(--navy)"/><path d="M4 4 L6 4 L6.6 7 L5.4 8 C6 10 7 11.2 8.4 12 L9.4 10.8 L11.2 11.6 L11.2 14 C7 14.5 3.5 9 4 4 Z" fill="var(--lime-bright)"/></svg>
      <p class="lines"><span class="cta">For information call now</span><span class="phone">844-555-0172</span></p>
    </div>
  </section>

  <!-- Slide 02 -->
  <div class="slide-label" style="left:603px">SLIDE 02</div>
  <section class="slide" style="left:429px">
    <svg class="slide-art" viewBox="0 0 341 339">
      <defs>
        <linearGradient id="bg2" x1="0" y1="0" x2="0" y2="1"><stop offset="0" stop-color="#0a4aa0"/><stop offset=".6" stop-color="#073d8a"/></linearGradient>
        <radialGradient id="photo2" cx=".5" cy=".5" r=".6"><stop offset="0" stop-color="#d9874a"/><stop offset=".7" stop-color="#b7632e"/><stop offset="1" stop-color="#8f4a22"/></radialGradient>
      </defs>
      <rect width="341" height="339" fill="url(#bg2)"/>
      <path d="M0,168 C45,258 110,300 170,300 C230,300 296,258 341,168 L341,339 L0,339 Z" fill="#ffffff"/>
      <path d="M0,192 C55,270 115,312 170,312 C225,312 290,272 341,192 L341,339 L0,339 Z" fill="var(--lime-bright)"/>
      <circle cx="170" cy="189" r="114" fill="none" stroke="var(--gold)" stroke-width=".7"/>
      <circle cx="170" cy="189" r="108" fill="var(--deep-blue)"/>
      <circle cx="170" cy="189" r="105" fill="url(#photo2)" role="img" aria-label="Top-down photo of children on a wooden floor using tablets, phones and a laptop"/>
      <g fill="#c8d6ee"><circle cx="18" cy="15" r=".8"/><circle cx="23" cy="15" r=".8"/><circle cx="28" cy="15" r=".8"/><circle cx="33" cy="15" r=".8"/><circle cx="18" cy="20" r=".8"/><circle cx="23" cy="20" r=".8"/><circle cx="28" cy="20" r=".8"/><circle cx="33" cy="20" r=".8"/><circle cx="18" cy="25" r=".8"/><circle cx="23" cy="25" r=".8"/><circle cx="28" cy="25" r=".8"/><circle cx="33" cy="25" r=".8"/>
      <circle cx="310" cy="15" r=".8"/><circle cx="315" cy="15" r=".8"/><circle cx="320" cy="15" r=".8"/><circle cx="325" cy="15" r=".8"/><circle cx="310" cy="20" r=".8"/><circle cx="315" cy="20" r=".8"/><circle cx="320" cy="20" r=".8"/><circle cx="325" cy="20" r=".8"/><circle cx="310" cy="25" r=".8"/><circle cx="315" cy="25" r=".8"/><circle cx="320" cy="25" r=".8"/><circle cx="325" cy="25" r=".8"/></g>
    </svg>
    <h2 class="headline" style="top:15px"><span class="accent" style="font-size:23px;line-height:1.2">Less Buffering</span><span class="main" style="font-size:23px;line-height:1.2">While Streaming</span></h2>
    <p class="feature feature-support">Real<br>Customer<br><span class="hl">Support</span></p>
    <p class="feature feature-speed">Fast Web<br><span class="hl">Browsing</span></p>
    <div class="brand-tag"><span class="dot"></span><span class="name">Brimfox Networks</span></div>
    <div class="contact">
      <svg viewBox="0 0 13 19"><rect width="13" height="19" rx="1.5" fill="var(--navy)"/><path d="M4 4 L6 4 L6.6 7 L5.4 8 C6 10 7 11.2 8.4 12 L9.4 10.8 L11.2 11.6 L11.2 14 C7 14.5 3.5 9 4 4 Z" fill="var(--lime-bright)"/></svg>
      <p class="lines"><span class="cta">For information call now</span><span class="phone">844-555-0172</span></p>
    </div>
  </section>

  <!-- Slide 03 -->
  <div class="slide-label" style="left:963px">SLIDE 03</div>
  <section class="slide" style="left:792px">
    <svg class="slide-art" viewBox="0 0 341 339">
      <defs>
        <linearGradient id="bg3" x1="0" y1="0" x2="0" y2="1"><stop offset="0" stop-color="#0a4aa0"/><stop offset=".6" stop-color="#073d8a"/></linearGradient>
        <linearGradient id="photo3" x1="0" y1="0" x2="0" y2="1"><stop offset="0" stop-color="#3c6aa8"/><stop offset=".18" stop-color="#c98a5a"/><stop offset=".3" stop-color="#1d2a44"/><stop offset="1" stop-color="#14223a"/></linearGradient>
      </defs>
      <rect width="341" height="339" fill="url(#bg3)"/>
      <path d="M0,168 C45,258 110,300 170,300 C230,300 296,258 341,168 L341,339 L0,339 Z" fill="#ffffff"/>
      <path d="M0,192 C55,270 115,312 170,312 C225,312 290,272 341,192 L341,339 L0,339 Z" fill="var(--lime-bright)"/>
      <circle cx="170" cy="189" r="114" fill="none" stroke="var(--gold)" stroke-width=".7"/>
      <circle cx="170" cy="189" r="108" fill="var(--deep-blue)"/>
      <circle cx="170" cy="189" r="105" fill="url(#photo3)" role="img" aria-label="Aerial photo of a city at dusk with glowing network connection arcs"/>
      <g fill="#c8d6ee"><circle cx="18" cy="15" r=".8"/><circle cx="23" cy="15" r=".8"/><circle cx="28" cy="15" r=".8"/><circle cx="33" cy="15" r=".8"/><circle cx="18" cy="20" r=".8"/><circle cx="23" cy="20" r=".8"/><circle cx="28" cy="20" r=".8"/><circle cx="33" cy="20" r=".8"/><circle cx="18" cy="25" r=".8"/><circle cx="23" cy="25" r=".8"/><circle cx="28" cy="25" r=".8"/><circle cx="33" cy="25" r=".8"/>
      <circle cx="310" cy="15" r=".8"/><circle cx="315" cy="15" r=".8"/><circle cx="320" cy="15" r=".8"/><circle cx="325" cy="15" r=".8"/><circle cx="310" cy="20" r=".8"/><circle cx="315" cy="20" r=".8"/><circle cx="320" cy="20" r=".8"/><circle cx="325" cy="20" r=".8"/><circle cx="310" cy="25" r=".8"/><circle cx="315" cy="25" r=".8"/><circle cx="320" cy="25" r=".8"/><circle cx="325" cy="25" r=".8"/></g>
    </svg>
    <h2 class="headline" style="top:20px"><span class="accent" style="font-size:18px;line-height:1.3">No Introductory Charges,</span><span class="main" style="font-size:18px;line-height:1.3">One Constant Rate</span></h2>
    <p class="feature feature-support">Real<br>Customer<br><span class="hl">Support</span></p>
    <p class="feature feature-speed">Fast Web<br><span class="hl">Browsing</span></p>
    <div class="brand-tag"><span class="dot"></span><span class="name">Brimfox Networks</span></div>
    <div class="contact">
      <svg viewBox="0 0 13 19"><rect width="13" height="19" rx="1.5" fill="var(--navy)"/><path d="M4 4 L6 4 L6.6 7 L5.4 8 C6 10 7 11.2 8.4 12 L9.4 10.8 L11.2 11.6 L11.2 14 C7 14.5 3.5 9 4 4 Z" fill="var(--lime-bright)"/></svg>
      <p class="lines"><span class="cta">For information call now</span><span class="phone">844-555-0172</span></p>
    </div>
  </section>

</main>
</body>
</html>
```